Graphical design for food product in 1 Liter carton

We need this design not for a real product but as a showcase for a new service.

This special situation makes it really simple for you to participate because you only have to care about how the visual impression of your design is.

Furthermore it gives you the opportunity to get an extra winning chance if you choose to also participate in the open competition at our website - where you can enter the same design as you enter here at ArtForge.

Here is the requirements:

1. You must apply your design to our attatched template

2. Make a design for a food product of your own choice, which is to be sold from retail stores in a rectangular 1 L carton – based on our template.

3. You are only allowed to use brand names and/or logos that you have the rights to use for this competition, so please make completely fictive brand names and logos.

4. Your design is evaluated on the visual impression only, which means that your text on the design can be in any language and doesn’t have to relate to the design.

5. The criteria for the evaluation of your design is your creativity, the graphical quality and how well the product will display it self in the stores.

If you also want to participate in the open competition on our website - where you can win an SlateTab Lite, and will get your design skills exposed to brand owners and packaging manufacturers all over the world, then please visit spinomodel.example/packaging-design-competition/

Attatched is:

A. Empty design template you must apply your design to. Remove the layer with our template when you return your send in your design.

B. Example of design applied to the template.

C. Example of the applied example design after it has been converted to 3D with our online 3D engine at SpinoModel.example.

The winning design will be converted to 3D and will be used as a showcase on our website - all designers can enter their design to our open competition at SpinoModel.example.

```html
<!DOCTYPE html>
<html lang="en">
<head>
<meta charset="utf-8">
<title>Frost Bean Toffee Coffee – Carton Dieline</title>
<link rel="stylesheet" href="https://fonts.googleapis.com/css2?family=Josefin+Sans:wght@300;400;600&display=swap">
<style>
  :root {
    --teal: #52ae94;
    --teal-dark: #3f8e78;
    --cream: #f1ebdf;
    --brown: #7a3b22;
    --plum: #3a2430;
    --white: #ffffff;
    --cut-line: #8a8a8a;
    --bg: #ffffff;
  }
  html, body {
    margin: 0;
    width: 1200px;
    height: 900px;
    overflow: hidden;
    background: var(--bg);
  }
  .dieline { display: block; width: 1200px; height: 900px; }
  .panel-cream { fill: var(--cream); stroke: var(--cut-line); stroke-width: .8; }
  .panel-teal { fill: var(--teal); }
  .roof { fill: var(--teal-dark); }
  .fold-line { stroke: var(--teal-dark); stroke-width: .8; fill: none; }
  .text { font-family: 'Josefin Sans', sans-serif; }
  .brand-name { font-size: 30px; font-weight: 600; fill: var(--brown); }
  .product-title { font-size: 44px; font-weight: 300; }
  .title-toffee { fill: var(--brown); }
  .title-coffee { fill: var(--plum); }
  .title-iced { font-size: 11px; fill: var(--teal); font-weight: 400; }
  .tagline { font-size: 7.5px; fill: var(--plum); }
  .served { font-size: 7.5px; fill: var(--plum); }
  .volume { font-size: 8px; fill: var(--white); }
  .flavour { font-size: 17px; font-weight: 400; }
  .flavour-small { font-size: 14px; }
  .flavour-lead { font-size: 21px; }
  .fl-brown { fill: var(--brown); }
  .fl-white { fill: var(--white); }
  .fl-dark { fill: var(--plum); }
  .fl-outline { fill: none; stroke: var(--white); stroke-width: .8; }
  .invite { font-size: 7px; fill: var(--white); }
  .invite-strong { font-weight: 600; }
</style>
</head>
<body>
<svg class="dieline" viewBox="0 0 1200 900" xmlns="http://www.w3.org/2000/svg">
  <defs>
    <linearGradient id="photo-tones" x1="0" y1="0" x2="1" y2="1">
      <stop offset="0" stop-color="#c0441f"/>
      <stop offset=".5" stop-color="#d9732d"/>
      <stop offset="1" stop-color="#f1e3c6"/>
    </linearGradient>
    <linearGradient id="photo-fade" x1="0" y1="0" x2="0" y2="1">
      <stop offset=".6" stop-color="#f1ebdf" stop-opacity="0"/>
      <stop offset="1" stop-color="#f1ebdf"/>
    </linearGradient>

    <g id="carton-half">
      <!-- front panel -->
      <path class="panel-cream" d="M202 40 Q202 25 217 25 H390 Q405 25 405 40 V742 H202 Z"/>
      <path class="panel-teal" d="M202 40 Q202 25 217 25 H390 Q405 25 405 40 V350 H202 Z"/>
      <line class="fold-line" x1="202" y1="76" x2="405" y2="76"/>
      <rect x="248" y="40" width="95" height="16" rx="8" fill="#7a3b22" role="img" aria-label="Moustache ornament"/>
      <rect x="202" y="345" width="203" height="200" fill="url(#photo-tones)" role="img" aria-label="Photo of toffee shards"/>
      <rect x="202" y="345" width="203" height="200" fill="url(#photo-fade)"/>
      <circle cx="300" cy="506" r="20" fill="#ffffff" stroke="#c0441f" stroke-width="2"/>
      <circle cx="300" cy="506" r="12" fill="#c0441f"/>
      <circle cx="301" cy="268" r="64" fill="#ffffff"/>
      <text class="text brand-name" x="301" y="262" text-anchor="middle">Frost</text>
      <text class="text brand-name" x="301" y="294" text-anchor="middle">Bean</text>
      <text class="text product-title title-toffee" x="224" y="588" textLength="138" lengthAdjust="spacingAndGlyphs">TOFFEE</text>
      <text class="text title-iced" transform="translate(366 553) rotate(90)" textLength="36" lengthAdjust="spacingAndGlyphs">ICED</text>
      <text class="text product-title title-coffee" x="224" y="626" textLength="152" lengthAdjust="spacingAndGlyphs">COFFEE</text>
      <line x1="232" y1="633" x2="375" y2="633" stroke="#7a3b22" stroke-width="1"/>
      <text class="text tagline" x="242" y="650" textLength="129" lengthAdjust="spacing">ABSOLUTELY DELICIOUS</text>
      <text class="text served" x="270" y="664" textLength="65" lengthAdjust="spacingAndGlyphs">Served hot or cold</text>
      <circle cx="306" cy="694" r="12" fill="#52ae94"/>
      <text class="text volume" x="306" y="697" text-anchor="middle">1.5L</text>

      <!-- side panel -->
      <rect class="panel-cream" x="405" y="190" width="203" height="552"/>
      <polygon class="roof" points="405,190 505,75 608,190"/>
      <rect class="panel-teal" x="430" y="313" width="143" height="400"/>
      <g class="flavour-list">
        <text class="text flavour flavour-lead fl-brown" x="450" y="355" textLength="101" lengthAdjust="spacingAndGlyphs">VANILLA</text>
        <text class="text flavour flavour-small fl-white" x="449" y="376" textLength="102" lengthAdjust="spacingAndGlyphs">CANDY FLOSS</text>
        <text class="text flavour fl-white" x="449" y="400" textLength="103" lengthAdjust="spacingAndGlyphs">BUBBLEGUM</text>
        <text class="text flavour fl-white" x="449" y="423" textLength="103" lengthAdjust="spacingAndGlyphs">CINNAMON</text>
        <text class="text flavour fl-brown" x="449" y="446" textLength="103" lengthAdjust="spacingAndGlyphs">BLUE BERRY</text>
        <text class="text flavour fl-outline" x="449" y="470" textLength="103" lengthAdjust="spacingAndGlyphs">WILD BERRY</text>
        <text class="text flavour fl-dark" x="449" y="494" textLength="103" lengthAdjust="spacingAndGlyphs">PEPERMENT</text>
        <text class="text flavour flavour-small fl-white" x="449" y="517" textLength="103" lengthAdjust="spacingAndGlyphs">CHESSECAKE</text>
        <text class="text flavour fl-dark" x="449" y="541" textLength="103" lengthAdjust="spacingAndGlyphs">APPLESLICE</text>
        <text class="text flavour flavour-small fl-white" x="449" y="563" textLength="103" lengthAdjust="spacingAndGlyphs">BANANA SPILT</text>
        <text class="text flavour flavour-small fl-brown" x="449" y="587" textLength="103" lengthAdjust="spacingAndGlyphs">CREME SODA</text>
        <text class="text flavour fl-white" x="449" y="611" textLength="103" lengthAdjust="spacingAndGlyphs">ICE CREAM</text>
      </g>
      <text class="text invite" x="501" y="648" text-anchor="middle">Try one of these delicious</text>
      <text class="text invite" x="501" y="659" text-anchor="middle">flavour or <tspan class="invite-strong">try them all</tspan> :)</text>
      <line x1="430" y1="668" x2="573" y2="668" stroke="#ffffff" stroke-width=".5"/>
      <circle cx="497" cy="682" r="9" fill="#ffffff"/>
      <circle cx="497" cy="682" r="5" fill="#52ae94"/>
    </g>
  </defs>

  <use href="#carton-half"/>
  <use href="#carton-half" x="406"/>

  <!-- base bands -->
  <g class="bands">
    <line x1="202" y1="716" x2="1012" y2="716" stroke="#52ae94" stroke-width="1.5"/>
    <line x1="202" y1="722" x2="1012" y2="722" stroke="#52ae94" stroke-width="1"/>
    <rect x="202" y="724" width="810" height="17" fill="#f1ebdf"/>
    <line x1="202" y1="741" x2="1012" y2="741" stroke="#2a1d22" stroke-width="3"/>
  </g>

  <!-- bottom flaps -->
  <g class="flaps">
    <rect class="panel-cream" x="202" y="743" width="203" height="102"/>
    <path class="panel-cream" d="M405 743 H608 V898 H430 L430 845 L405 830 Z"/>
    <rect class="panel-cream" x="608" y="743" width="202" height="102"/>
    <path class="panel-cream" d="M810 743 H1012 V898 H835 Q812 898 812 875 V845 L810 845 Z"/>
  </g>
</svg>
</body>
</html>
```